Breezeway Climate Business Card Design

Design new, 2 sides, business cards for a residential and light commercial heating, air conditioning contractor.

Target Market(s)

Homeowners, small businesses

Industry/Entity Type

Business

Contact Information for Business Card

Dominic Vasquerelli
Phone - 555-214-6837
Email
Address - PO box 618
Millbrook NJ 07999
Website - www.BreezewayClimateLLC.example

Requirements
Must have
• logo, company colors, standard size with no die cut, so I can use printhaven

```html
<!DOCTYPE html>
<html lang="en">
<head>
<meta charset="utf-8">
<title>Breezeway Climate Business Card</title>
<link rel="stylesheet" href="https://fonts.googleapis.com/css2?family=Roboto:wght@400;500;700&family=Roboto+Slab:wght@700&display=swap">
<style>
  :root {
    --backdrop: #e4e4e4;
    --card-black: #0a0a0c;
    --maroon: #7e2a2a;
    --maroon-deep: #6e2322;
    --orange: #e8891f;
    --flame-red: #d8391f;
    --gold: #f3c02d;
    --cream: #f6d97a;
    --band-text: #f2c75c;
    --white: #f7f1ea;
    --ink-maroon: #6a1f1f;
  }
  * { margin: 0; padding: 0; box-sizing: border-box; }
  html, body {
    width: 1200px; height: 576px; overflow: hidden;
    background: var(--backdrop);
  }
  .canvas { position: relative; width: 1200px; height: 576px; }

  .card { position: absolute; top: 138px; width: 484px; height: 293px; overflow: hidden; }

  /* Front */
  .card-front { left: 81px; background: var(--card-black); }
  .front-brand {
    position: absolute; left: 0; right: 0; top: 108px;
    text-align: center;
    font-family: "Roboto Slab", serif; font-weight: 700;
    font-size: 34px; line-height: 38px; color: var(--cream);
  }
  .front-band {
    position: absolute; left: 0; right: 0; top: 246px; height: 27px;
    background: var(--maroon);
    display: flex; align-items: center; justify-content: center;
    font-family: "Roboto", sans-serif; font-size: 12px; color: var(--band-text);
    letter-spacing: 0.1px;
  }

  /* Back */
  .card-back { left: 602px; background: var(--maroon); }
  .back-wave { position: absolute; inset: 0; }
  .services {
    position: absolute; right: 22px; top: 18px;
    text-align: right;
    font-family: "Roboto", sans-serif; font-weight: 700;
    font-size: 12px; line-height: 16px; color: var(--ink-maroon);
  }
  .services .mark { display: inline-block; width: 14px; text-align: right; font-weight: 500; }
  .holder-name {
    position: absolute; left: 21px; top: 68px;
    font-family: "Roboto Slab", serif; font-weight: 700;
    font-size: 19px; color: var(--gold);
  }
  .holder-title {
    position: absolute; left: 21px; top: 93px;
    font-family: "Roboto", sans-serif; font-size: 10.5px; color: var(--white);
  }
  .contact-list {
    position: absolute; left: 24px; top: 196px; list-style: none;
    font-family: "Roboto", sans-serif; font-size: 12px; color: var(--white);
  }
  .contact-list li { display: flex; align-items: center; height: 17.4px; }
  .contact-list svg { width: 11px; height: 11px; margin-right: 9px; fill: var(--gold); flex: none; }
  .back-brand {
    position: absolute; left: 268px; width: 196px; top: 190px;
    text-align: center;
    font-family: "Roboto Slab", serif; font-weight: 700;
    font-size: 24px; line-height: 27px; color: var(--cream);
  }
</style>
</head>
<body>
<main class="canvas">

  <section class="card card-front" aria-label="Business card front">
    <p class="front-brand">Breezeway<br>Climate</p>
    <p class="front-band">Residential &amp; Light Commercial Heating &nbsp;• Air Conditioning Contractor</p>
  </section>

  <section class="card card-back" aria-label="Business card back">
    <svg class="back-wave" viewBox="0 0 484 293" preserveAspectRatio="none" aria-hidden="true">
      <path d="M0,0 H484 V128 C420,124 370,100 320,72 C260,40 180,22 100,22 C60,22 25,26 0,32 Z" fill="var(--orange)"/>
      <path d="M0,30 C60,14 150,10 250,34 C200,24 110,22 40,34 Z" fill="var(--flame-red)"/>
      <path d="M0,32 C60,22 150,18 230,30 C150,26 70,30 0,40 Z" fill="var(--maroon-deep)"/>
      <path d="M40,36 C140,20 250,34 320,74 C380,108 430,124 484,128" fill="none" stroke="var(--cream)" stroke-width="3"/>
    </svg>

    <p class="services">
      Residential and Light <span class="mark">«</span><br>
      Commercial Heating <span class="mark"></span><br>
      Air Conditioning <span class="mark">«</span><br>
      Contractor <span class="mark"></span>
    </p>

    <h1 class="holder-name">Dominic Vasquerelli</h1>
    <p class="holder-title">Managing Director</p>

    <ul class="contact-list">
      <li>
        <svg viewBox="0 0 24 24"><path d="M4 9c0-4 3-6 8-6s8 2 8 6l-4 1-1-3H9L8 10 4 9zm3 3h10l3 8H4l3-8zm5 2a2.5 2.5 0 100 5 2.5 2.5 0 000-5z"/></svg>
        555-214-6837
      </li>
      <li>
        <svg viewBox="0 0 24 24"><path d="M2 5h20v14H2V5zm2 2v.5l8 5.5 8-5.5V7H4z"/></svg>
        info@BreezewayClimateLLC.example
      </li>
      <li>
        <svg viewBox="0 0 24 24"><path d="M12 1a8 8 0 00-8 8c0 6 8 14 8 14s8-8 8-14a8 8 0 00-8-8zm0 5a3 3 0 110 6 3 3 0 010-6z"/></svg>
        PO box 618 Millbrook NJ 07999
      </li>
      <li>
        <svg viewBox="0 0 24 24"><path d="M12 2a10 10 0 100 20 10 10 0 000-20zm0 2c1 1.3 1.8 3.3 2 6h-4c.2-2.7 1-4.7 2-6zM4.1 11h3.9c.1 2 .5 3.7 1.1 5.2A8 8 0 014.1 11zm0-2A8 8 0 019 4.8 15 15 0 008 9H4.1zM10 11h4c-.1 2.8-1 5-2 6.5-1-1.5-1.9-3.7-2-6.5zm6 0h3.9a8 8 0 01-5 5.2c.6-1.5 1-3.2 1.1-5.2zm0-2a15 15 0 00-1-4.2A8 8 0 0119.9 9H16z"/></svg>
        BreezewayClimateLLC.example
      </li>
    </ul>

    <p class="back-brand">Breezeway<br>Climate</p>
  </section>

</main>
</body>
</html>
```